Postcard Flyer needed to promote exceptional new chef in London gastropub

We need a double sided postcard style flyer to tell local residents about our new menu and head chef. The idea is to inform local residents about the new food offering, as well as showcasing the venue and garden going into summer.
The venue is a Victorian coaching Inn. We have moved the food offering upmarket but whilst we aim to showcase the best of British cuisine, we want to retain our heritage as a pub.
Our head chef Tobias has experience working at some of the world’s best restaurants including Maison Forel, London; Copper Heron, Moscow; Dorian Pleck at the Halworth; and Quill, Mayfair.
Tobias's aim is to make sure that every dish, from the humble to the refined, is the best it can possibly be.
We have some good photography and would like to make the flyer very image led. The back would need to have a location map of some kind.
Our venue is the Fenwick Arms in NW27, London

Target Market(s)

Affluent local residents and businesses.

Industry/Entity Type

Chef

Colors

Designer to choose colors to be used in the design.

Requirements
Must have
• Hard hitting visual appeal. Location map and contact on the back. Standard print ready postcard size with print bleeds.

```html
<!DOCTYPE html>
<html lang="en">
<head>
<meta charset="utf-8">
<title>Fenwick Arms – New Head Chef Postcard</title>
<link href="https://fonts.googleapis.com/css2?family=Tinos:wght@400;700&family=Zilla+Slab:wght@600;700&display=swap" rel="stylesheet">
<style>
  :root {
    --page: #eceef0;
    --charcoal: #2c2c30;
    --charcoal-deep: #1f1f22;
    --gold: #d4a64a;
    --gold-soft: #c9a35a;
    --gold-light: #f0d596;
    --body-text: #e6e4df;
    --map-tone: #4a4a50;
  }
  * { box-sizing: border-box; margin: 0; padding: 0; }
  html, body { width: 1200px; height: 898px; overflow: hidden; }
  body { background: var(--page); position: relative; font-family: "Tinos", "Times New Roman", serif; }

  .card {
    position: absolute; top: 53px; width: 551px; height: 781px; overflow: hidden;
    box-shadow: 0 2px 6px rgba(0,0,0,.18);
  }
  .card--front { left: 31px; }
  .card--back { left: 618px; background: linear-gradient(160deg, #343439 0%, var(--charcoal) 55%, #28282c 100%); }

  /* Front */
  .venue-photo {
    position: absolute; inset: 0;
    background: linear-gradient(180deg, #6d9fd8 0%, #a9c8e8 22%, #ece7dc 38%, #e9e2d2 52%, #2b2a2a 62%, #3a3533 78%, #8a5a35 90%, #6b4a35 100%);
  }
  .badge {
    position: absolute; left: 71px; top: 43px; width: 408px; height: 408px; border-radius: 50%;
    background: linear-gradient(135deg, var(--gold-light), var(--gold) 45%, #a9772a 100%);
    padding: 8px;
  }
  .badge__inner {
    position: relative; width: 100%; height: 100%; border-radius: 50%;
    background: radial-gradient(circle at 40% 35%, #2f2f33, var(--charcoal-deep));
    overflow: hidden;
  }
  .badge__brand {
    position: absolute; left: 0; right: 0; top: 114px; text-align: center;
    font-family: "Zilla Slab", Georgia, serif; font-weight: 600; font-size: 24px;
    letter-spacing: 3px; color: var(--gold); text-transform: uppercase;
  }
  .badge__intro {
    position: absolute; left: 72px; top: 162px;
    font-family: "Zilla Slab", Georgia, serif; font-weight: 700; font-size: 18.5px;
    line-height: 21px; color: #fff; letter-spacing: .4px;
  }
  .badge__chef {
    position: absolute; left: 72px; top: 204px;
    font-family: "Zilla Slab", Georgia, serif; font-weight: 700; font-size: 28px;
    color: var(--gold);
  }
  .badge__rule {
    position: absolute; left: 0; right: 0; top: 262px; height: 2px; background: var(--gold);
  }
  .badge__history {
    position: absolute; left: 72px; top: 292px; width: 262px;
    font-size: 12px; line-height: 16px; color: var(--gold-soft);
  }

  /* Back */
  .back__headline {
    position: absolute; left: 38px; top: 44px; z-index: 2;
    font-size: 21px; line-height: 25.5px; color: var(--gold); font-weight: 400;
  }
  .dish-photo {
    position: absolute; left: 30px; top: 75px; width: 496px; height: 496px; border-radius: 50%;
    background: radial-gradient(circle at 50% 50%, #efe8cf 0%, #d8c99a 14%, #4a4a4e 26%, #38383c 60%, #2f2f33 100%);
  }
  .back__copy {
    position: absolute; left: 38px; top: 525px; width: 476px;
    font-size: 13.6px; line-height: 17.4px; color: var(--body-text); text-align: justify;
  }
  .back__copy p + p { margin-top: 17px; }
  .contact {
    position: absolute; top: 690px; font-size: 12.4px; line-height: 15.6px; color: var(--body-text); font-style: normal;
  }
  .contact--address { left: 38px; }
  .contact--online { left: 286px; }
  .location-map {
    position: absolute; left: 446px; top: 684px; width: 80px; height: 66px;
    background: var(--map-tone); border: 1px solid var(--gold);
  }
</style>
</head>
<body>

<section class="card card--front">
  <div class="venue-photo" role="img" aria-label="Photograph of the Victorian pub frontage in sunshine with a courtyard garden of wooden picnic benches and planters"></div>
  <div class="badge">
    <div class="badge__inner">
      <div class="badge__brand">The Fenwick Arms</div>
      <h1 class="badge__intro">The Fenwick Arms is proud to<br>introduce our new head chef</h1>
      <div class="badge__chef">Tobias Marsh</div>
      <div class="badge__rule"></div>
      <p class="badge__history">Formerly at Maison Forel, London; Copper Heron, Moscow; Dorian Pleck at the Halworth; and Quill, Mayfair.</p>
    </div>
  </div>
</section>

<section class="card card--back">
  <div class="dish-photo" role="img" aria-label="Photograph of a plated dessert with cream, honeycomb, crumb and edible flowers on a dark speckled stoneware plate"></div>
  <h2 class="back__headline">The Fenwick Arms<br>is delighted to welcome<br>the exceptionally talented<br>Tobias Marsh to the team.</h2>
  <div class="back__copy">
    <p>Tobias is using his experience of working at some of the world’s best restaurants to create stunning seasonal menus that showcase the best of modern British cooking, while reflecting our heritage as a pub. His aim is to make sure that every dish, from the humble to the refined, is the best it can possibly be.</p>
    <p>Whether you’re looking for a quick lunch in the courtyard garden; diner in the wood panelled dining room; or a lazy Sunday Roast; we hope to welcome you to the pub this Summer to try Tobias’s fantastic food.</p>
  </div>
  <address class="contact contact--address">Fenwick Arms,<br>48 Alder Row, London NW27 5SW<br>020 7946 0321</address>
  <address class="contact contact--online">info@fenwick-arms.co.uk<br>www.fenwick-arms.co.uk</address>
  <div class="location-map" role="img" aria-label="Location map showing the Fenwick Arms on Alder Row, London NW27"></div>
</section>

</body>
</html>
```